Brain Science Music company needs modern clean website

We're looking for a website that's very clean and modern but also has some nice bold (futuristic) colors in it. The design should communicate a company that's providing something new and fresh! We'd greatly appreciate web designs similar to: https://thebrightfolio.co/

Lumen Cascade is a US-based Neuroscience music company that offers state-of-the-art technology solutions that help people focus, relax and sleep with the help of scientifically engineered music.

Target Market(s)

US businesses looking for specialized neuroscience music technology.

Logo Text

LumenCascade or LC

Coding

Coded - Design and coding required

Number of Pages Required

1 page

Font styles to use
Sans Serif

Colors

Designer to choose colors to be used in the design.

Requirements
Nice to have
• A website similar to: https://thebrightfolio.co/
We like the colors, the fonts, the simple design layouts and the colorful images.

```html
<!DOCTYPE html>
<html lang="en">
<head>
<meta charset="UTF-8">
<title>Lumen Cascade — The new frontier of music and the brain</title>
<link rel="stylesheet" href="https://fonts.googleapis.com/css2?family=Roboto:wght@400;500;700;900&family=Lato:wght@400;700&display=swap">
<style>
  :root {
    --purple: #4a14d8;
    --purple-soft: #e3dcfa;
    --pink: #ef1f5c;
    --ink: #1d1d22;
    --body: #3a3a44;
    --white: #ffffff;
    --footer: #1e1e1e;
  }
  * { box-sizing: border-box; margin: 0; padding: 0; }
  html, body { width: 1200px; height: 3627px; overflow: hidden; background: var(--white); }
  body { font-family: "Lato", sans-serif; color: var(--body); }
  .page { position: relative; width: 1200px; height: 3627px; overflow: hidden; }
  .abs { position: absolute; }

  /* Header */
  .site-header { position: absolute; left: 0; top: 0; width: 1200px; height: 84px; }
  .brand { position: absolute; left: 145px; top: 22px; display: flex; align-items: center; gap: 12px;
    font-family: "Roboto", sans-serif; font-weight: 500; font-size: 25px; color: var(--ink); }
  .brand-dot { width: 38px; height: 38px; border-radius: 50%; background: var(--purple); }
  .main-nav { position: absolute; top: 34px; left: 0; width: 1200px; font-family: "Roboto", sans-serif;
    font-weight: 500; font-size: 13.5px; color: var(--ink); }
  .main-nav span { position: absolute; white-space: nowrap; }
  .main-nav .active { color: var(--purple); }

  /* Hero */
  .hero-art { position: absolute; left: 0; top: 84px; }
  .hero-title { position: absolute; left: 802px; top: 200px; font-family: "Roboto", sans-serif; font-weight: 700;
    font-size: 64px; line-height: 62px; letter-spacing: -0.5px; }
  .hero-title .l1 { color: var(--purple); display: block; }
  .hero-title .l2 { color: var(--pink); display: block; }
  .hero-tagline { position: absolute; left: 803px; top: 346px; font-family: "Roboto", sans-serif; font-size: 35px;
    line-height: 41px; color: var(--ink); }
  .btn-pill { position: absolute; left: 805px; top: 455px; width: 167px; height: 42px; border-radius: 21px;
    background: var(--pink); color: var(--white); font-family: "Roboto", sans-serif; font-weight: 700; font-size: 15px;
    display: flex; align-items: center; justify-content: center; box-shadow: 0 6px 14px rgba(239,31,92,.3); }
  .slider-dots { position: absolute; left: 805px; top: 536px; display: flex; gap: 10px; align-items: center; }
  .slider-dots span { width: 13px; height: 13px; border-radius: 50%; background: var(--ink); }
  .slider-dots .current { width: 26px; height: 26px; border: 2px solid var(--pink); background: var(--white); position: relative; }
  .slider-dots .current::after { content: ""; position: absolute; left: 5px; top: 5px; width: 12px; height: 12px; border-radius: 50%; background: var(--pink); }

  /* Section headings */
  .section-title { position: absolute; left: 0; width: 1200px; text-align: center; font-family: "Roboto", sans-serif;
    font-weight: 700; font-size: 38px; color: var(--ink); }
  .rule { position: absolute; height: 4px; width: 62px; background: var(--purple); }

  /* Applications */
  .apps-sub { position: absolute; top: 830px; left: 0; width: 1200px; text-align: center; font-family: "Roboto", sans-serif;
    font-size: 16px; color: var(--ink); }
  .app { position: absolute; top: 895px; width: 190px; text-align: center; }
  .app svg { display: block; margin: 0 auto; }
  .app-label { margin-top: 18px; font-family: "Roboto", sans-serif; font-weight: 700; font-size: 15.5px; letter-spacing: .5px; color: var(--ink); }

  /* Entrainment */
  .entrain-bg { position: absolute; left: 0; top: 1239px; }
  .card { position: absolute; top: 1494px; width: 231px; height: 397px; background: var(--white); padding: 8px; }
  .card-media { width: 215px; height: 165px; }
  .card-badge { position: absolute; left: 72px; top: 150px; width: 86px; height: 86px; border-radius: 50%; background: var(--pink);
    border: 4px solid var(--white); display: flex; align-items: center; justify-content: center; }
  .card-text { position: absolute; left: 12px; right: 12px; top: 259px; text-align: center; font-size: 15.5px; line-height: 22.5px; color: var(--ink); }

  /* Story */
  .story-title { position: absolute; left: 148px; top: 2166px; font-family: "Roboto", sans-serif; font-weight: 500; font-size: 39px; color: var(--ink); }
  .story-body { position: absolute; left: 148px; top: 2264px; width: 440px; font-size: 14.6px; line-height: 24px; color: var(--body); }
  .story-body p { margin-bottom: 16px; }

  /* Newsletter */
  .newsletter { position: absolute; left: 0; top: 2935px; width: 1200px; height: 433px;
    background: radial-gradient(ellipse at 15% 60%, #f3e3f7 0%, rgba(243,227,247,0) 45%),
                radial-gradient(ellipse at 85% 70%, #e1f0f5 0%, rgba(225,240,245,0) 45%),
                linear-gradient(180deg, #dcd9f2 0%, #ece6f6 55%, #e7eef6 100%); }
  .news-title { position: absolute; top: 117px; left: 0; width: 1200px; text-align: center; font-family: "Roboto", sans-serif;
    font-weight: 900; font-size: 47px; letter-spacing: 1px; color: var(--ink); }
  .news-sub { position: absolute; top: 185px; left: 0; width: 1200px; text-align: center; font-family: "Roboto", sans-serif;
    font-size: 19px; line-height: 29px; color: var(--ink); }
  .email-field { position: absolute; left: 273px; top: 264px; width: 472px; height: 55px; background: var(--white);
    box-shadow: 0 3px 10px rgba(0,0,0,.12); padding-left: 30px; display: flex; align-items: center; font-size: 14.5px; color: #777; }
  .btn-subscribe { position: absolute; left: 769px; top: 264px; width: 157px; height: 55px; background: var(--pink);
    color: var(--white); font-family: "Roboto", sans-serif; font-weight: 700; font-size: 17px; display: flex; align-items: center; justify-content: center;
    box-shadow: 0 3px 10px rgba(239,31,92,.3); }

  /* Footer */
  .site-footer { position: absolute; left: 0; top: 3368px; width: 1200px; height: 259px; background: var(--footer); color: #e8e8e8; font-size: 17px; }
  .contacts { position: absolute; top: 59px; left: 0; width: 1200px; display: flex; justify-content: center; gap: 38px; }
  .contacts span { display: flex; align-items: center; gap: 10px; }
  .copyright { position: absolute; top: 104px; left: 0; width: 1200px; text-align: center; }
  .socials { position: absolute; top: 155px; left: 0; width: 1200px; display: flex; justify-content: center; gap: 10px; }
  .socials span { width: 42px; height: 42px; border-radius: 50%; border: 1.5px solid #d8d8d8; }
</style>
</head>
<body>
<div class="page">

  <header class="site-header">
    <div class="brand"><span class="brand-dot"></span>Lumen Cascade</div>
    <nav class="main-nav">
      <span class="active" style="left:548px">HOME</span>
      <span style="left:617px">ABOUT US</span>
      <span style="left:714px">APPLICATIONS</span>
      <span style="left:842px">CASE STUDIES</span>
      <span style="left:967px">CONTACT US</span>
    </nav>
  </header>

  <!-- Hero -->
  <svg class="hero-art" width="720" height="610" viewBox="0 0 720 610" role="img" aria-label="Woman wearing headphones in profile, dissolving into a cosmic field of stars and crystals">
    <defs>
      <linearGradient id="heroFill" x1="0" y1="0" x2="1" y2="0.3">
        <stop offset="0" stop-color="#2a2060"/>
        <stop offset="0.35" stop-color="#1b1a3c"/>
        <stop offset="0.7" stop-color="#2a2a3a"/>
        <stop offset="1" stop-color="#ffffff" stop-opacity="0"/>
      </linearGradient>
      <radialGradient id="heroGlow" cx="0.15" cy="0.35" r="0.4">
        <stop offset="0" stop-color="#c24ec8" stop-opacity=".7"/>
        <stop offset="1" stop-color="#c24ec8" stop-opacity="0"/>
      </radialGradient>
    </defs>
    <path d="M0 0 H720 V420 C660 460 620 470 590 460 C540 440 500 400 440 395 C380 392 330 470 270 520 C220 560 160 615 110 598 C70 585 40 560 0 560 Z" fill="url(#heroFill)"/>
    <path d="M0 0 H400 V400 C330 470 270 520 210 560 C160 600 100 605 60 580 C30 565 10 560 0 560 Z" fill="url(#heroGlow)"/>
  </svg>

  <h1 class="hero-title"><span class="l1">Lumen</span><span class="l2">Cascade</span></h1>
  <p class="hero-tagline">The new frontier of<br>music and the brain</p>
  <div class="btn-pill">LEARN MORE</div>
  <div class="slider-dots"><span class="current"></span><span></span><span></span><span></span></div>

  <!-- Applications -->
  <h2 class="section-title" style="top:745px">Applications</h2>
  <div class="rule" style="left:569px;top:806px"></div>
  <p class="apps-sub">Merging neuroscience and music, creating audio enhancing</p>

  <div class="app" style="left:137px">
    <svg width="180" height="180" viewBox="0 0 180 180" aria-hidden="true">
      <path d="M80 8 C130 2 170 30 165 90 C160 150 120 178 70 172 C25 166 5 130 8 90 C11 45 35 12 80 8Z" fill="var(--purple-soft)"/>
      <path d="M90 14 C140 8 178 40 175 92 C172 140 140 168 92 164 C45 160 8 140 8 95 C8 50 40 20 90 14Z" fill="var(--purple)"/>
      <g fill="none" stroke="#fff" stroke-width="5" stroke-linecap="round">
        <rect x="60" y="70" width="22" height="40" rx="11"/><line x1="66" y1="110" x2="66" y2="135"/>
        <rect x="106" y="70" width="22" height="40" rx="11"/><line x1="122" y1="110" x2="122" y2="135"/>
        <path d="M72 52 Q94 36 116 52"/><path d="M64 40 Q94 18 124 40"/>
      </g>
    </svg>
    <div class="app-label">PRODUCTIVITY</div>
  </div>
  <div class="app" style="left:382px">
    <svg width="180" height="180" viewBox="0 0 180 180" aria-hidden="true">
      <path d="M80 8 C130 2 170 30 165 90 C160 150 120 178 70 172 C25 166 5 130 8 90 C11 45 35 12 80 8Z" fill="var(--purple-soft)"/>
      <path d="M90 14 C140 8 178 40 175 92 C172 140 140 168 92 164 C45 160 8 140 8 95 C8 50 40 20 90 14Z" fill="var(--purple)"/>
      <path d="M78 48 A45 45 0 1 0 138 112 A38 38 0 0 1 78 48Z" fill="none" stroke="#fff" stroke-width="5" stroke-linejoin="round"/>
      <g fill="none" stroke="#fff" stroke-width="4" stroke-linejoin="round">
        <path d="M96 62 H108 L96 76 H108"/><path d="M114 72 H124 L114 84 H124"/><path d="M132 52 H144 L132 66 H144"/>
      </g>
    </svg>
    <div class="app-label">SLEEP</div>
  </div>
  <div class="app" style="left:627px">
    <svg width="180" height="180" viewBox="0 0 180 180" aria-hidden="true">
      <path d="M80 8 C130 2 170 30 165 90 C160 150 120 178 70 172 C25 166 5 130 8 90 C11 45 35 12 80 8Z" fill="var(--purple-soft)"/>
      <path d="M90 14 C140 8 178 40 175 92 C172 140 140 168 92 164 C45 160 8 140 8 95 C8 50 40 20 90 14Z" fill="var(--purple)"/>
      <g fill="none" stroke="#fff" stroke-width="4" stroke-linecap="round">
        <circle cx="92" cy="88" r="30"/><circle cx="92" cy="88" r="14"/>
        <path d="M50 140 Q92 118 134 140"/>
        <path d="M50 56 v10 M45 61 h10"/><path d="M134 52 v10 M129 57 h10"/>
      </g>
    </svg>
    <div class="app-label">MEDITATION</div>
  </div>
  <div class="app" style="left:872px">
    <svg width="180" height="180" viewBox="0 0 180 180" aria-hidden="true">
      <path d="M80 8 C130 2 170 30 165 90 C160 150 120 178 70 172 C25 166 5 130 8 90 C11 45 35 12 80 8Z" fill="var(--purple-soft)"/>
      <path d="M90 14 C140 8 178 40 175 92 C172 140 140 168 92 164 C45 160 8 140 8 95 C8 50 40 20 90 14Z" fill="var(--purple)"/>
      <g fill="none" stroke="#fff" stroke-width="5" stroke-linecap="round" stroke-linejoin="round">
        <path d="M48 92 H88 L104 60 L120 92 H140"/><path d="M128 80 L140 92 L128 104"/>
      </g>
    </svg>
    <div class="app-label">ATHLETICS</div>
  </div>

  <!-- Brainwave Entrainment -->
  <svg class="entrain-bg" width="1200" height="820" viewBox="0 0 1200 820" role="img" aria-label="Soft purple-to-pink backdrop with a faint woman's profile">
    <defs>
      <linearGradient id="entrainFill" x1="0" y1="0" x2="0.25" y2="1">
        <stop offset="0" stop-color="#5a2ad8"/>
        <stop offset="0.45" stop-color="#8a3cc6"/>
        <stop offset="0.8" stop-color="#d23a88"/>
        <stop offset="1" stop-color="#ee3a66"/>
      </linearGradient>
    </defs>
    <path d="M0 55 C70 48 120 42 200 38 C320 32 400 20 520 8 C600 0 660 0 720 20 C760 35 770 60 810 56 C870 50 900 32 960 32 C1030 32 1060 45 1110 40 C1160 34 1185 18 1200 10
             L1200 790 C1130 792 1070 812 980 814 C880 816 820 770 720 770 C640 770 560 800 440 798 C340 796 280 760 200 776 C140 790 80 812 40 800 C20 795 8 788 0 790 Z" fill="url(#entrainFill)"/>
  </svg>

  <h2 class="section-title" style="top:1383px;color:var(--white)">Brainwave Entrainment</h2>
  <div class="rule" style="left:569px;top:1444px;background:var(--white)"></div>

  <div class="card" style="left:112px">
    <div class="card-media" role="img" aria-label="Illustration of two heads exchanging gears and ideas" style="background:linear-gradient(135deg,#2a9fd8 0%,#7cc6e8 50%,#f08a24 100%)"></div>
    <div class="card-badge"><svg width="40" height="40" viewBox="0 0 40 40" aria-hidden="true"><g fill="none" stroke="#fff" stroke-width="2.5"><circle cx="20" cy="20" r="14"/><circle cx="20" cy="20" r="6"/></g></svg></div>
    <p class="card-text">Neurons in our brains communicate with each other, forming thoughts, emotions, and ideas using electrical impulses</p>
  </div>
  <div class="card" style="left:360px">
    <div class="card-media" role="img" aria-label="Illustration of a head silhouette over a pattern of gears" style="background:linear-gradient(135deg,#f08ad8 0%,#c548c8 45%,#3ac8d8 100%)"></div>
    <div class="card-badge"><svg width="40" height="40" viewBox="0 0 40 40" aria-hidden="true"><g fill="none" stroke="#fff" stroke-width="2.5" stroke-linecap="round"><circle cx="20" cy="18" r="12"/><path d="M10 34 H30"/></g></svg></div>
    <p class="card-text">Activities such as sleeping, working, or meditating, each have their own unique brainwave pattern.</p>
  </div>
  <div class="card" style="left:608px">
    <div class="card-media" role="img" aria-label="Illustration of a head silhouette over a circuit board pattern" style="background:linear-gradient(135deg,#e83aa8 0%,#b84ad0 45%,#38c8e0 100%)"></div>
    <div class="card-badge"><svg width="40" height="40" viewBox="0 0 40 40" aria-hidden="true"><g fill="none" stroke="#fff" stroke-width="2.5" stroke-linecap="round"><path d="M20 34 V20 M20 20 L12 10 M20 20 L28 10 M20 20 V6"/><circle cx="12" cy="10" r="2.5"/><circle cx="28" cy="10" r="2.5"/></g></svg></div>
    <p class="card-text">Lumen Cascade leverages Musical Phase Locking, to optimize brainwave patterns for each desired activity</p>
  </div>
  <div class="card" style="left:856px">
    <div class="card-media" role="img" aria-label="Glowing brain scan over colourful audio equaliser bars" style="background:linear-gradient(135deg,#0a2a6a 0%,#1c5ab8 50%,#102a5a 100%)"></div>
    <div class="card-badge"><svg width="40" height="40" viewBox="0 0 40 40" aria-hidden="true"><g fill="none" stroke="#fff" stroke-width="2.5" stroke-linecap="round"><path d="M17 28 V10 L28 8 V24"/><circle cx="14" cy="28" r="3.5"/><circle cx="25" cy="24" r="3.5"/></g></svg></div>
    <p class="card-text">Our music is driven by science. We utilize large scale studies and data from electro-encephlograms to produce substantial results</p>
  </div>

  <!-- Founder story -->
  <h2 class="story-title">Marcus's Story</h2>
  <div class="rule" style="left:148px;top:2236px"></div>
  <div class="story-body">
    <p>Founder and Team Leader of Lumen Cascade, in conjunction with primary scientific advisor Dr. Helen Varga. Marcus is a pioneer in the neuroscience of music, and key innovator on the technology of Musical Phase Locking.</p>
    <p>At the age of 10, Marcus wrote his first symphony and began studying music composition</p>
    <p>After exposure to alpha waves in music, Marcus began a lifelong pursuit of merging neuroscience and music composition</p>
    <p>Marcus founded Clearline Labs in 2003, creating audio workstations for those who wanted to experience the effects of music guided by neuroscience, as well as software for brain-computer interfaces..</p>
    <p>As the science progressed and Clearline Labs grew, Marcus decided to form Wavefold.io in 2014, a website and app that allowed nearly anybody to access the music, not just those who were scientifically minded.</p>
    <p>Lumen Cascade was formed to further the vision of neuroscience-based music becoming a daily resource that everyone should experience.</p>
  </div>

  <svg class="abs" style="left:612px;top:2183px" width="588" height="636" viewBox="0 0 588 636" role="img" aria-label="Portrait of the founder, a smiling bearded man in glasses and a denim shirt at his desk">
    <defs>
      <linearGradient id="founderFill" x1="0" y1="0" x2="1" y2="1">
        <stop offset="0" stop-color="#f6dcec"/>
        <stop offset="0.4" stop-color="#6a7fb0"/>
        <stop offset="0.75" stop-color="#2e4d84"/>
        <stop offset="1" stop-color="#d8423a"/>
      </linearGradient>
    </defs>
    <path d="M300 4 C380 0 450 60 500 150 C560 250 600 360 570 460 C540 560 460 630 350 634 C240 638 110 600 50 510 C0 430 0 340 10 260 C25 150 110 90 190 40 C230 15 260 6 300 4Z" fill="url(#founderFill)"/>
  </svg>

  <!-- Newsletter -->
  <section class="newsletter">
    <h2 class="news-title">JOIN OUR NEWSLETTER</h2>
    <p class="news-sub">Subscribe to our mailing list to receive updates<br>and promotional offers.</p>
    <div class="email-field">Enter your E - mail</div>
    <div class="btn-subscribe">SUBSCRIBE</div>
  </section>

  <!-- Footer -->
  <footer class="site-footer">
    <div class="contacts">
      <span><svg width="12" height="16" viewBox="0 0 12 16" aria-hidden="true"><path d="M6 0 C2.7 0 0 2.6 0 5.8 C0 10 6 16 6 16 S12 10 12 5.8 C12 2.6 9.3 0 6 0Z M6 8 A2.2 2.2 0 1 1 6 3.6 A2.2 2.2 0 0 1 6 8Z" fill="#e8e8e8"/></svg>Lumen Cascade, enim ipsam, 6018</span>
      <span><svg width="14" height="14" viewBox="0 0 14 14" aria-hidden="true"><path d="M3 0 L5.5 3.5 L4 5 C5 7 7 9 9 10 L10.5 8.5 L14 11 L12 14 C6 13.5 0.5 8 0 2Z" fill="#e8e8e8"/></svg>808-555-0142</span>
      <span><svg width="15" height="11" viewBox="0 0 15 11" aria-hidden="true"><rect width="15" height="11" rx="1" fill="#e8e8e8"/><path d="M0.5 1 L7.5 6 L14.5 1" fill="none" stroke="#1e1e1e" stroke-width="1.3"/></svg>info@lumencascade.com</span>
    </div>
    <p class="copyright">© 2021 Lumen Cascade. All Rights Reserved.</p>
    <div class="socials" aria-label="Social links"><span></span><span></span><span></span></div>
  </footer>

</div>
</body>
</html>
```